Social Media designs (LinkedIn banner, LinkedIn posts, Instagram)

Hello designers!
We are looking to create some more concepts for our social media identity for a search firm (recruitment company)
I have attached a "brand toolkit" that shows our brand, logo, colour scheme to guide you with regards to colours and identiy.

You will see in the brand toolkit there are some examples of;
- A LinkedIn banner for the company (page 23)
- Social Media posts for LinkedIn and Instagram (page 21)

What we are looking for...

We don't really like the current LinkedIn banner ideas. We would like to see more concepts that look more aesthetically pleasing - the current ideas look quite dull.

We DO like the social media post concepts but we would like to have more templates/options that we can use (similar themes)

We welcome submissions for Social Media designs that we can use with our company branding. Thank you for your work in advance!

```html
<!DOCTYPE html>
<html lang="en">
<head>
<meta charset="UTF-8">
<title>Harlow Reed — Talent Knows No Borders</title>
<link rel="stylesheet" href="https://fonts.googleapis.com/css2?family=Outfit:wght@500;600;700&display=swap">
<style>
  :root {
    --bg-deep: #1b2925;
    --bg-mid: #23352f;
    --bg-haze: #2c423a;
    --brand-green: #4f8f75;
    --brand-green-soft: #5a9b80;
    --line-white: rgba(236, 244, 240, 0.85);
    --portrait-light: #3d5e50;
    --portrait-dark: #1e322b;
  }
  html, body {
    margin: 0;
    padding: 0;
    overflow: hidden;
    background: var(--bg-deep);
  }
  .post {
    position: relative;
    width: 1200px;
    height: 1200px;
    overflow: hidden;
    background: var(--bg-deep);
    font-family: "Outfit", "Helvetica Neue", Arial, sans-serif;
  }
  .backdrop {
    position: absolute;
    inset: 0;
    background:
      radial-gradient(ellipse 70% 35% at 40% 62%, var(--bg-haze) 0%, transparent 70%),
      linear-gradient(180deg, var(--bg-deep) 0%, var(--bg-mid) 48%, var(--bg-haze) 60%, var(--bg-mid) 78%, var(--bg-deep) 100%);
  }
  .guides {
    position: absolute;
    inset: 0;
    width: 1200px;
    height: 1200px;
  }
  .brand {
    position: absolute;
    top: 34px;
    left: 36px;
    display: flex;
    align-items: center;
    gap: 18px;
  }
  .brand-mark {
    width: 44px;
    height: 44px;
    background: var(--brand-green);
  }
  .brand-name {
    color: var(--brand-green-soft);
    font-weight: 500;
    font-size: 32px;
    line-height: 1.05;
    letter-spacing: 0.2px;
  }
  .headline {
    position: absolute;
    left: 104px;
    top: 272px;
    margin: 0;
    color: var(--brand-green);
    font-weight: 700;
    text-transform: uppercase;
    line-height: 1;
  }
  .headline span { display: block; }
  .headline .line-small {
    font-size: 124px;
    letter-spacing: 1px;
    line-height: 1.06;
  }
  .headline .line-big {
    font-size: 430px;
    line-height: 0.78;
    letter-spacing: -6px;
    margin: 14px 0 8px -8px;
  }
  .portrait {
    position: absolute;
    left: 706px;
    top: 162px;
    width: 494px;
    height: 1038px;
    border-radius: 200px 200px 0 0;
    background: linear-gradient(180deg, var(--portrait-light) 0%, var(--portrait-dark) 55%, #16251f 100%);
  }
</style>
</head>
<body>
  <main class="post">
    <div class="backdrop" role="img" aria-label="Dimmed landscape of an open road stretching to distant hills, tinted green"></div>

    <svg class="guides" viewBox="0 0 1200 1200" aria-hidden="true">
      <path d="M0 324 A780 780 0 0 1 408 142" fill="none" stroke="var(--line-white)" stroke-width="1.5"/>
      <line x1="408" y1="142" x2="408" y2="1200" stroke="var(--line-white)" stroke-width="1.5"/>
      <path d="M408 566 A360 360 0 0 0 132 1200" fill="none" stroke="var(--line-white)" stroke-width="1.5"/>
      <line x1="0" y1="926" x2="124" y2="926" stroke="var(--line-white)" stroke-width="1.5"/>
    </svg>

    <header class="brand">
      <div class="brand-mark"></div>
      <div class="brand-name">Harlow<br>Reed</div>
    </header>

    <h1 class="headline">
      <span class="line-small">Talent</span>
      <span class="line-small">Knows</span>
      <span class="line-big">No</span>
      <span class="line-small">Borders</span>
    </h1>

    <div class="portrait" role="img" aria-label="Smiling bearded businessman in a dark suit and tie, arms crossed, tinted green"></div>
  </main>
</body>
</html>
```